Website Design for new Custom Homebuilder company R Pelbrook Homes

We need a website design for a new company based out of Liberty Hill, Texas called R Pelbrook Homes. We specialize in building unique, high end custom homes in Liberty Hill, Texas and the surrounding area. We would like to see designs that use the color black, white, copper and gold. Website needs to have a modern feel and the pages that have information about the company and then pages that have a gallery with pictures of completed homes and a page that has information on available homes.

```html
<!DOCTYPE html>
<html lang="en">
<head>
<meta charset="utf-8">
<title>R Pelbrook Homes</title>
<link href="https://fonts.googleapis.com/css2?family=Barlow:wght@400;500;600&display=swap" rel="stylesheet">
<style>
:root{
  --copper:#a2673f;
  --black:#000;
  --ink:#1d1d1d;
  --muted:#555;
  --white:#fff;
  --line:#cfcfcf;
  --soft:#ccc;
}
*{box-sizing:border-box;margin:0;padding:0}
html,body{width:1200px;height:3270px;overflow:hidden}
body{font-family:'Barlow',sans-serif;color:var(--ink);background:var(--white);position:relative}
.abs{position:absolute}
.brand{font-weight:500;font-size:22px;color:var(--copper);display:flex;align-items:center;gap:10px;letter-spacing:.5px}
.brand i{display:block;width:14px;height:14px;background:var(--copper)}
.nav{display:flex;gap:38px;font-size:14px;color:var(--ink);align-items:center}
.nav .active{color:var(--copper)}
.btn{background:var(--copper);color:var(--white);font-size:15px;font-weight:500;display:flex;align-items:center;justify-content:center;gap:8px}
.btn svg{width:16px;height:10px}
.eyebrow{color:var(--copper);font-size:20px;letter-spacing:.3px}
h1,h2{font-weight:500;line-height:1.2}
.section-title{font-size:41px;font-weight:500;line-height:46px}
.vlabel{writing-mode:vertical-rl;transform:rotate(180deg);color:var(--copper);font-size:14px;letter-spacing:2px;display:flex;align-items:center;gap:14px}
.vlabel::before{content:"";width:2px;height:22px;background:currentColor}
.vlabel.light{color:var(--white)}
.dark{background:var(--black);color:var(--white)}
.arrows{display:flex;gap:4px}
.arrows span{width:41px;height:40px;display:flex;align-items:center;justify-content:center;border:1px solid var(--copper)}
.arrows span.on{background:var(--copper)}
.arrows svg{width:20px;height:12px}
.feature-num{color:var(--copper);font-size:18px;font-weight:600;margin-bottom:8px}
.card-cap{background:var(--white);box-shadow:0 6px 18px rgba(0,0,0,.12);padding:12px 16px}
.card-cap .meta{font-size:12px;color:var(--muted);display:flex;gap:10px}
.card-cap .meta b{color:var(--copper);font-weight:400}
.card-cap h3{font-size:17px;font-weight:500;line-height:1.15;margin-top:6px}
.field{border:1px solid var(--line);font-size:12px;color:#555;padding:0 12px;display:flex;align-items:center;gap:8px;background:var(--white)}
.field svg{width:11px;height:11px;fill:#888}
.info{display:flex;gap:14px;font-size:14px;color:var(--white);align-items:flex-start}
.info svg{width:14px;height:14px;fill:var(--white);flex:none;margin-top:2px}
.footer-head{color:var(--copper);font-size:16px;font-weight:500}
.links li{list-style:none;font-size:14px;color:var(--soft);display:flex;align-items:center;gap:10px;height:38px}
.links li::before{content:"";width:4px;height:4px;border-radius:50%;background:var(--copper)}
.social{width:11px;height:11px;border-radius:50%;background:var(--copper)}
</style>
</head>
<body>

<header>
  <div class="abs brand" style="left:173px;top:40px"><i></i>R Pelbrook Homes</div>
  <nav class="abs nav" style="left:548px;top:29px">
    <span class="active">Home</span><span>About</span><span>Gallery</span><span>Blog</span><span>Contact</span>
    <span style="display:flex;gap:10px;align-items:center;font-size:13px"><svg width="12" height="12" viewBox="0 0 24 24" fill="#a2673f"><path d="M6.6 10.8a15 15 0 0 0 6.6 6.6l2.2-2.2c.3-.3.7-.4 1-.2 1.1.4 2.3.6 3.6.6.6 0 1 .4 1 1V20c0 .6-.4 1-1 1A17 17 0 0 1 3 4c0-.6.4-1 1-1h3.5c.6 0 1 .4 1 1 0 1.3.2 2.5.6 3.6.1.3 0 .7-.2 1z"/></svg>512-555-0148</span>
  </nav>
</header>

<section class="hero">
  <div class="abs" style="left:28px;top:216px;font-size:16px;line-height:39px">
    <div style="color:var(--copper);display:flex;align-items:center;gap:10px">01<span style="width:18px;height:2px;background:var(--copper)"></span></div>
    <div>02</div><div>03</div>
  </div>
  <div class="abs eyebrow" style="left:175px;top:197px">WE SPECIALIZE IN</div>
  <h1 class="abs" style="left:175px;top:222px;font-size:33px;font-weight:500;line-height:40px">Building unique,<br>High end Custom<br>Homes in Liberty Hill</h1>
  <div class="abs btn" style="left:175px;top:372px;width:149px;height:43px">Take A Tour <svg viewBox="0 0 16 10"><path d="M0 5h14M10 1l4 4-4 4" stroke="#fff" fill="none" stroke-width="1.4"/></svg></div>
  <svg class="abs" style="left:478px;top:92px" width="696" height="386" viewBox="0 0 696 386">
    <defs><linearGradient id="heroSky" x1="0" y1="0" x2="0" y2="1"><stop offset="0" stop-color="#a58a7a"/><stop offset=".6" stop-color="#c8b7aa"/><stop offset="1" stop-color="#6d5646"/></linearGradient></defs>
    <polygon role="img" aria-label="Two-storey white custom home with lit wooden porch at dusk" points="12,386 12,150 339,10 686,150 686,386" fill="url(#heroSky)"/>
    <polyline points="2,386 2,146 339,2 694,146 694,386" fill="none" stroke="#a2673f" stroke-width="2.5"/>
  </svg>
</section>

<section class="abs dark welcome" style="left:0;top:568px;width:1200px;height:432px">
  <div class="abs vlabel" style="left:170px;top:67px">WELCOME</div>
  <div class="abs" role="img" aria-label="Yellow clapboard family home with green lawn" style="left:203px;top:67px;width:440px;height:292px;background:linear-gradient(170deg,#cfd9c4,#d9b66a 45%,#5f7d3a)"></div>
  <h2 class="abs" style="left:682px;top:85px;font-size:41px;font-weight:500">R Pelbrook Homes</h2>
  <p class="abs" style="left:683px;top:139px;width:340px;font-size:14px;line-height:22.5px">Nullam suscipit sapien a libero efficitur, vel bibendum sapien condimentum. Duis in odio accumsan, feugiat massa vel, placerat quam. Etiam ac mi risus. Nam quis dapibus dui. In sollicitudin, ligula non aliquet finibus, dolor justo vulputate orci, eget placerat mauris justo quis urna.</p>
  <div class="abs btn" style="left:688px;top:293px;width:148px;height:43px">Read More <svg viewBox="0 0 16 10"><path d="M0 5h14M10 1l4 4-4 4" stroke="#fff" fill="none" stroke-width="1.4"/></svg></div>
</section>

<section class="abs features" style="left:0;top:1000px;width:1200px;height:412px">
  <div class="abs vlabel" style="left:170px;top:72px">FEATURES</div>
  <h2 class="abs section-title" style="left:208px;top:64px">Special features<br>for our Customer</h2>
  <div class="abs" style="left:211px;top:170px;display:grid;grid-template-columns:188px 188px;row-gap:32px;font-size:14px;line-height:20px">
    <div><div class="feature-num">01</div>Luxurious interior<br>design and amenities</div>
    <div><div class="feature-num">02</div>Private balconies with<br>stunning views</div>
    <div><div class="feature-num">03</div>Living rooms are<br>pre-wired for Surround</div>
    <div><div class="feature-num">04</div>A rare combination of<br>inspired architecture</div>
  </div>
  <div class="abs" role="img" aria-label="Grand stone mansion with arched windows and driveway" style="left:610px;top:71px;width:416px;height:270px;background:linear-gradient(180deg,#7fb0dd,#cfd8dd 50%,#9a9690)"></div>
</section>

<section class="abs dark gallery" style="left:0;top:1412px;width:1200px;height:463px">
  <h2 class="abs" style="left:169px;top:57px;font-size:41px;font-weight:500">Property Gallery</h2>
  <div class="abs arrows" style="left:941px;top:69px">
    <span><svg viewBox="0 0 20 12"><path d="M20 6H2M6 1 1 6l5 5" stroke="#a2673f" fill="none" stroke-width="1.4"/></svg></span>
    <span class="on"><svg viewBox="0 0 20 12"><path d="M0 6h18M14 1l5 5-5 5" stroke="#fff" fill="none" stroke-width="1.4"/></svg></span>
  </div>
  <div class="abs" role="img" aria-label="Modern white home with balconies" style="left:399px;top:125px;width:200px;height:263px;background:linear-gradient(180deg,#9fb6d1,#e5e5e3 55%,#8c7b67)"></div>
  <div class="abs" role="img" aria-label="Luxury bedroom interior with warm lighting" style="left:599px;top:125px;width:214px;height:263px;background:linear-gradient(180deg,#e6ddd0,#a98760 60%,#5a4332)"></div>
  <div class="abs" role="img" aria-label="Glass-fronted A-frame house with pool at dusk" style="left:813px;top:125px;width:214px;height:263px;background:linear-gradient(180deg,#3f5a85,#7a8aa0 55%,#8a6a46)"></div>
  <div class="abs" role="img" aria-label="Modern grey home with white facade and lawn" style="left:161px;top:111px;width:238px;height:290px;box-shadow:0 10px 30px rgba(255,255,255,.12);background:linear-gradient(180deg,#7f96ae,#c7cdd2 45%,#6f8a56 70%,#3d4a5a)"></div>
</section>

<section class="abs blog" style="left:0;top:1875px;width:1200px;height:582px">
  <div class="abs vlabel" style="left:170px;top:75px">BLOG</div>
  <h2 class="abs section-title" style="left:208px;top:66px">Follow the latest<br>Articles &amp; Blog</h2>
  <div class="abs arrows" style="left:941px;top:100px">
    <span><svg viewBox="0 0 20 12"><path d="M20 6H2M6 1 1 6l5 5" stroke="#a2673f" fill="none" stroke-width="1.4"/></svg></span>
    <span class="on"><svg viewBox="0 0 20 12"><path d="M0 6h18M14 1l5 5-5 5" stroke="#fff" fill="none" stroke-width="1.4"/></svg></span>
  </div>
  <div class="abs" role="img" aria-label="Brick and timber two-storey house under blue sky" style="left:173px;top:187px;width:265px;height:331px;background:linear-gradient(180deg,#9cc3e4,#4b5566 45%,#d8c7a8 70%,#6f9a4e)"></div>
  <div class="abs" role="img" aria-label="Bedroom with large window and wooden floor" style="left:469px;top:187px;width:264px;height:331px;background:linear-gradient(180deg,#d6d8da,#5d6169 45%,#c9bfb2 70%,#7a4b2a)"></div>
  <div class="abs" role="img" aria-label="Living room with grey sofa and marble feature wall" style="left:763px;top:187px;width:266px;height:331px;background:linear-gradient(180deg,#e9e4dc,#8d7260 50%,#7c7e86 75%,#3a2d26)"></div>
  <div class="abs card-cap" style="left:193px;top:452px;width:224px;height:87px"><div class="meta"><b>▣</b>January 18, 2022 <span><b>●</b> By admin</span></div><h3>Phasellus mollis sed lectus</h3></div>
  <div class="abs card-cap" style="left:489px;top:452px;width:224px;height:87px"><div class="meta"><b>▣</b>January 18, 2022 <span><b>●</b> By admin</span></div><h3>Phasellus mollis sed lectus</h3></div>
  <div class="abs card-cap" style="left:784px;top:452px;width:224px;height:87px"><div class="meta"><b>▣</b>January 18, 2022 <span><b>●</b> By admin</span></div><h3>Phasellus mollis sed lectus</h3></div>
</section>

<section class="abs contact" style="left:0;top:2457px;width:1200px;height:414px">
  <div class="abs" style="left:0;top:0;width:541px;height:414px;background:var(--copper)"></div>
  <div class="abs vlabel light" style="left:170px;top:45px">CONTACT</div>
  <h2 class="abs section-title" style="left:204px;top:42px;color:var(--white)">Request for<br>More Information</h2>
  <p class="abs" style="left:173px;top:160px;width:340px;font-size:14px;line-height:19px;color:var(--white)">Lorem ipsum dolor sit amet, consectetur adipiscing elit. Sed sollicitudin nunc ut eros gravida, quis tempor mi condimentum.</p>
  <div class="abs" style="left:173px;top:238px;display:flex;flex-direction:column;gap:15px">
    <div class="info"><svg viewBox="0 0 24 24"><path d="M12 2a7 7 0 0 0-7 7c0 5 7 13 7 13s7-8 7-13a7 7 0 0 0-7-7zm0 9.5A2.5 2.5 0 1 1 12 6a2.5 2.5 0 0 1 0 5.5z"/></svg><span style="line-height:22px">318 Cedar Hollow Road<br>Liberty Hill, Texas 78642</span></div>
    <div class="info"><svg viewBox="0 0 24 24"><path d="M6.6 10.8a15 15 0 0 0 6.6 6.6l2.2-2.2c.3-.3.7-.4 1-.2 1.1.4 2.3.6 3.6.6.6 0 1 .4 1 1V20c0 .6-.4 1-1 1A17 17 0 0 1 3 4c0-.6.4-1 1-1h3.5c.6 0 1 .4 1 1 0 1.3.2 2.5.6 3.6.1.3 0 .7-.2 1z"/></svg>512-555-0148</div>
    <div class="info"><svg viewBox="0 0 24 24"><path d="M2 5h20v14H2zm2 2v.5l8 5 8-5V7z"/></svg>hello@rpelbrookhomes.com</div>
    <div class="info"><svg viewBox="0 0 24 24"><path d="M12 2a10 10 0 1 0 0 20 10 10 0 0 0 0-20zm7 9h-3a15 15 0 0 0-1.4-6A8 8 0 0 1 19 11zM12 4c1 1.4 1.8 4 2 7h-4c.2-3 1-5.6 2-7zM9.4 5A15 15 0 0 0 8 11H5a8 8 0 0 1 4.4-6zM5 13h3a15 15 0 0 0 1.4 6A8 8 0 0 1 5 13zm7 7c-1-1.4-1.8-4-2-7h4c-.2 3-1 5.6-2 7zm2.6-1a15 15 0 0 0 1.4-6h3a8 8 0 0 1-4.4 6z"/></svg>www.rpelbrookhomes.com</div>
  </div>
  <h2 class="abs" style="left:563px;top:52px;font-size:41px;font-weight:500">Get In Touch</h2>
  <div class="abs field" style="left:560px;top:103px;width:229px;height:36px"><svg viewBox="0 0 24 24"><circle cx="12" cy="7" r="5"/><path d="M2 22c0-6 5-9 10-9s10 3 10 9z"/></svg>First Name</div>
  <div class="abs field" style="left:799px;top:103px;width:228px;height:36px"><svg viewBox="0 0 24 24"><circle cx="12" cy="7" r="5"/><path d="M2 22c0-6 5-9 10-9s10 3 10 9z"/></svg>Last Name</div>
  <div class="abs field" style="left:560px;top:150px;width:229px;height:37px"><svg viewBox="0 0 24 24"><path d="M6.6 10.8a15 15 0 0 0 6.6 6.6l2.2-2.2c.3-.3.7-.4 1-.2 1.1.4 2.3.6 3.6.6.6 0 1 .4 1 1V20c0 .6-.4 1-1 1A17 17 0 0 1 3 4c0-.6.4-1 1-1h3.5c.6 0 1 .4 1 1 0 1.3.2 2.5.6 3.6.1.3 0 .7-.2 1z"/></svg>Phone No</div>
  <div class="abs field" style="left:799px;top:150px;width:228px;height:37px"><svg viewBox="0 0 24 24"><path d="M2 5h20v14H2zm2 2v.5l8 5 8-5V7z"/></svg>Email</div>
  <div class="abs field" style="left:560px;top:195px;width:467px;height:90px;align-items:flex-start;padding-top:10px"><svg viewBox="0 0 24 24"><path d="M3 17v4h4L19 9l-4-4z"/></svg>Your Message</div>
  <div class="abs btn" style="left:560px;top:301px;width:149px;height:45px">Send Message <svg viewBox="0 0 16 10"><path d="M0 5h14M10 1l4 4-4 4" stroke="#fff" fill="none" stroke-width="1.4"/></svg></div>
</section>

<footer class="abs dark" style="left:0;top:2871px;width:1200px;height:399px">
  <div class="abs brand" style="left:173px;top:72px"><i></i>R Pelbrook Homes</div>
  <p class="abs" style="left:173px;top:116px;width:300px;font-size:14px;line-height:21px;color:var(--soft)">Lorem ipsum dolor sit amet, consectetur adipiscing elit. Sed sollicitudin nunc ut eros gravida, quis tempor mi condimentum. In augue sapien, sollicitudin et convallis sit amet, lobortis et enim. Duis in odiccumsan, feugiat massa vel</p>
  <div class="abs footer-head" style="left:565px;top:74px">Useful Links</div>
  <ul class="abs links" style="left:565px;top:100px"><li>Home</li><li>About</li><li>Gallery</li><li>Blog</li><li>Contact</li></ul>
  <div class="abs footer-head" style="left:758px;top:74px">Subscribe Newsletter</div>
  <p class="abs" style="left:759px;top:105px;width:260px;font-size:14px;line-height:24px;color:var(--soft)">Subscribe to our newsletter &amp; always be aware of all the latest updates</p>
  <div class="abs field" style="left:759px;top:170px;width:268px;height:34px"><svg viewBox="0 0 24 24"><path d="M2 5h20v14H2zm2 2v.5l8 5 8-5V7z"/></svg>Enter email address</div>
  <div class="abs btn" style="left:759px;top:214px;width:268px;height:33px;font-size:14px">Subscribe <svg viewBox="0 0 16 10"><path d="M0 5h14M10 1l4 4-4 4" stroke="#fff" fill="none" stroke-width="1.4"/></svg></div>
  <div class="abs" style="left:173px;top:327px;width:854px;height:1px;background:#333"></div>
  <div class="abs" style="left:0;top:346px;width:1200px;text-align:center;font-size:13px;color:var(--soft)">© 2022 <span style="color:var(--copper)">R Pelbrook Homes</span>. All right reserved</div>
  <div class="abs" style="left:545px;top:374px;display:flex;gap:18px">
    <span class="social"></span><span class="social"></span><span class="social"></span><span class="social"></span>
  </div>
  <div class="abs" style="left:980px;top:340px;width:46px;height:46px;border-radius:50%;background:var(--copper);display:flex;align-items:center;justify-content:center"><svg width="18" height="12" viewBox="0 0 18 12"><path d="M2 10l7-7 7 7" stroke="#fff" stroke-width="2.4" fill="none"/></svg></div>
</footer>

</body>
</html>
```